CLU大学院「スキル羅針盤」のバナー作成 を作成していただける方を募集しております。 ■目的・概要 MBA取得検討者向け、ターゲティング広告用に、 コスモリンク大学大学院がプロデュースした「スキル羅針盤」の 新しいバナーの作成依頼です。 ■デザインイメージ 既存のバナーをご参考までに貼付いたします。 このバナーと同等かもしくはそれを上回るクオリティでの作成ができればと思います。 ランディング先のページは下記です。 サイト名:スキル羅針盤 URL: http://www.cosmolink-u.example/sk_lp/ スキル羅針盤は2万人を超える方々が実施しているコンテンツですので、 「診断者数2万人」などの要素をバナー内に入れていただいても結構です。 基本的には製作者様のセンスにお任せしたいと思います。 ■サイズ: 300×250 1枚 ■値段: 5000円 ■納品形式: PSDデータとJPGデータ ■継続について 今回コンペで採用された方には、引き続き他の10個以上のバナーの作成をお願いすることになるので、 ぜひふるってご応募くださいませ! 素敵なバナーになるよう、ぜひお力を貸してください。 たくさんのご応募お待ち致しております! |

```html
<!DOCTYPE html>
<html lang="ja">
<head>
<meta charset="utf-8">
<title>スキル羅針盤 バナー</title>
<link rel="stylesheet" href="https://fonts.googleapis.com/css2?family=Noto+Sans+JP:wght@500;700;900&family=Roboto+Condensed:ital,wght@0,400;0,700;1,400&family=Roboto+Mono&display=swap">
<style>
  :root{
    --sky-top:#f1f7fb;
    --sky-mid:#cfdfea;
    --city:#8ea3b4;
    --city-deep:#6d8497;
    --title-fill:#c3ecfb;
    --title-stroke:#4aa6d6;
    --panel:rgba(235,246,255,0.42);
    --panel-line:rgba(120,180,230,0.75);
    --ink-navy:#1d2f57;
    --ink-grey:#6b7380;
    --badge-a:#2f86d1;
    --badge-b:#7cc3f0;
    --button-a:#58b2ee;
    --button-b:#1f78c8;
    --white:#ffffff;
  }
  *{box-sizing:border-box;margin:0;padding:0}
  html,body{width:1200px;height:1000px;overflow:hidden;background:var(--white)}
  .banner{position:relative;width:1200px;height:1000px;overflow:hidden;font-family:"Noto Sans JP",sans-serif}
  .skyline{position:absolute;inset:0 0 111px 0;
    background:linear-gradient(180deg,var(--sky-top) 0%,var(--sky-mid) 38%,#a9bccb 60%,var(--city) 78%,var(--city-deep) 100%)}
  .panel{position:absolute;background:var(--panel);border:2px solid var(--panel-line);border-radius:6px;
    box-shadow:0 0 18px rgba(140,200,255,0.5)}
  .panel--code{left:278px;top:84px;width:190px;height:156px;padding:12px 14px;
    font-family:"Roboto Mono",monospace;font-size:11px;line-height:16px;color:#4f79a6}
  .panel--bars{left:818px;top:133px;width:142px;height:107px;background:rgba(255,255,255,0.8)}
  .panel--map{left:33px;top:333px;width:178px;height:100px;background:linear-gradient(135deg,rgba(210,230,245,0.75),rgba(170,205,235,0.75))}
  .panel--digits{left:989px;top:444px;width:193px;height:112px;padding:8px 10px;
    font-family:"Roboto Mono",monospace;font-size:12px;line-height:15px;color:#4d74a0;letter-spacing:0.5px}
  .panel--line{left:256px;top:667px;width:133px;height:100px}
  .panel--pie{left:767px;top:693px;width:155px;height:107px;background:rgba(245,250,255,0.7)}
  .panel svg{display:block;width:100%;height:100%}
  .title{position:absolute;left:0;right:0;top:262px;text-align:center;font-weight:500;font-size:136px;line-height:1;
    color:var(--title-fill);-webkit-text-stroke:3px var(--title-stroke);paint-order:stroke fill;
    text-shadow:0 0 10px #fff,0 0 22px #fff;letter-spacing:2px}
  .subtitle{position:absolute;left:0;right:0;top:446px;text-align:center;font-family:"Roboto Condensed",sans-serif;
    font-style:italic;font-weight:700;font-size:58px;line-height:1;color:var(--title-fill);
    -webkit-text-stroke:2px var(--title-stroke);paint-order:stroke fill;text-shadow:0 0 8px #fff}
  .tagline{position:absolute;left:0;right:0;top:576px;text-align:center;font-weight:900;font-size:36px;color:var(--white);
    -webkit-text-stroke:5px #2a3a55;paint-order:stroke fill;letter-spacing:0.5px}
  .accuracy{position:absolute;left:0;top:820px;width:478px;height:52px;border-radius:0 26px 26px 0;
    background:linear-gradient(90deg,var(--badge-a),var(--badge-b));color:var(--white);font-weight:700;font-size:33px;
    line-height:52px;padding-left:22px;box-shadow:0 0 10px rgba(255,255,255,0.7)}
  .footer{position:absolute;left:0;right:0;bottom:0;height:111px;background:var(--white)}
  .brand-mark{position:absolute;left:22px;top:12px;width:100px;text-align:center}
  .brand-mark .dot{width:50px;height:50px;border-radius:50%;background:var(--ink-navy);margin:0 auto 6px}
  .brand-mark .abbr{font-weight:700;font-size:24px;line-height:1;color:var(--ink-navy)}
  .school-name{position:absolute;left:176px;top:14px;font-weight:700;font-size:44px;line-height:1.1;color:var(--ink-navy)}
  .school-name-en{position:absolute;left:178px;top:68px;font-family:"Roboto Condensed",sans-serif;font-size:20px;
    letter-spacing:2.4px;color:var(--ink-grey)}
  .cta{position:absolute;left:846px;top:915px;width:332px;height:58px;border-radius:4px;
    background:linear-gradient(180deg,var(--button-a),var(--button-b));display:flex;align-items:center;gap:18px;
    padding-left:18px;color:var(--white);font-weight:700;font-size:28px}
  .cta svg{width:30px;height:30px;flex:none}
</style>
</head>
<body>
<main class="banner">
  <div class="skyline" role="img" aria-label="Photograph of a city skyline of office towers under a pale hazy sky"></div>

  <div class="panel panel--code">&lt;html lang=ja&gt;<br>&lt;head&gt;<br>&lt;meta charset&gt;<br>&lt;body&gt;<br>&lt;div id=top&gt;<br>&lt;h2&gt;<br>&lt;p&gt;<br>&lt;/div&gt;</div>

  <div class="panel panel--bars">
    <svg viewBox="0 0 142 107">
      <g fill="#6fb3e4">
        <rect x="22" y="70" width="16" height="22"/>
        <rect x="46" y="56" width="16" height="36"/>
        <rect x="70" y="42" width="16" height="50"/>
        <rect x="94" y="22" width="16" height="70"/>
      </g>
    </svg>
  </div>

  <div class="panel panel--map" role="img" aria-label="World map graphic"></div>

  <div class="panel panel--digits">7414226453253636237<br>2354381338693133318<br>9853591363463434463<br>1571335310315713064<br>5643759013364601358<br>8602760274967193471</div>

  <div class="panel panel--line">
    <svg viewBox="0 0 133 100">
      <polyline fill="none" stroke="#6fb3e4" stroke-width="3" points="10,70 25,40 38,62 52,30 66,58 80,26 94,54 108,36 122,50"/>
    </svg>
  </div>

  <div class="panel panel--pie">
    <svg viewBox="0 0 155 107">
      <circle cx="78" cy="54" r="36" fill="#ffffff" stroke="#6fb3e4" stroke-width="3"/>
      <path d="M78 54 L78 18 A36 36 0 0 1 114 54 Z" fill="#6fb3e4"/>
    </svg>
  </div>

  <h1 class="title">スキル羅針盤</h1>
  <p class="subtitle">~Find Your True Direction~</p>
  <p class="tagline">あなたの「ビジネススキル」や「志向性」が分かる！</p>

  <div class="accuracy">診断結果整合率84%!!</div>

  <footer class="footer">
    <div class="brand-mark"><div class="dot"></div><div class="abbr">CLU</div></div>
    <div class="school-name">コスモリンク大学大学院</div>
    <div class="school-name-en">Cosmolink Graduate School of Business</div>
  </footer>

  <a class="cta">
    <svg viewBox="0 0 30 30"><circle cx="15" cy="15" r="14" fill="#fff"/><path d="M12 9 L21 15 L12 21 Z" fill="#1f78c8"/></svg>
    無料診断実施中！
  </a>
</main>
</body>
</html>
```